Flyer für Freiwillige Feuerwehr
Zielgruppe
Freiwillige Feuerwehr/ Es soll zum einen die Jungen von 10 Jahren bis 16 sowie Erwachse von 16 Jahren bis open end Angesprochen werden
Aufgabenstellung
Es sollen zum einen die Erwachsenen und die Jugend auf einen Flyer geschickt angesprochen werden. Zum einen können wir mit dem Flyer die Kinder fangen und wenn die Eltern von den Kindern bzw. Erwachsene das lesen, dann könnten auch Sie angesprochen werden.
Inhalt für die Erwachsenen noch nicht Mitglieder:
Der Flyer sollte Verantwortung, Kameradschaft und eine gute berufliche oder ehrenamtliche Entwicklung betonen. Es geht hier um die Werbung von Personen, die bereit sind, sich aktiv in der Feuerwehr zu engagieren.
o Hauptaussage: 'Engagiere dich – Deine Feuerwehr braucht dich!' Möchtest du nur zusehen oder live dabei sein?!
o Visuelle Gestaltung: Zeige Bilder von aktiven Feuerwehrleuten im Einsatz, bei Einsätzen oder Trainings. Zeige Professionalität und Teamarbeit.
o Benefits: Überzeuge mit Aspekten wie Weiterbildungsmöglichkeiten, Teamarbeit, Verantwortung und gesellschaftlicher Beitrag.
o Call to Action (CTA): 'Mach den nächsten Schritt – Werde aktives Mitglied der Feuerwehr!'
o Kontaktinformationen: Eine einfache Möglichkeit zur Kontaktaufnahme, z.B. Telefonnummer für einen persönlichen Kontakt, E-Mail-Adresse oder QR-Code für Online-Anmeldung.
Inhalt für die Jugend:
Der Flyer muss ansprechend, modern und dynamisch sein, um Jugendliche zu motivieren. Junge Menschen interessieren sich oft für Abenteuer, Teamarbeit und den Beitrag zur Gemeinschaft.
• Hauptaussage: 'Werde Teil unseres Teams und erlebe spannende Abenteuer!'
• Visuelle Gestaltung: Bilder von jungen Feuerwehrmitgliedern in Aktion (z.B. Übungseinsätze, Abenteuer, Teamwork). Eine starke, klare Headline, z.B. 'Feuerwehr – Deine Chance für Action und Teamgeist!'
• Benefits: Betone, was die Jugend davon hat: Spaß, Herausforderungen, neue Freunde, Teilnahme an Übungen und Veranstaltungen.
• Call to Action (CTA): 'Komm zu uns! Wir suchen dich – Melde dich noch heute an!'
• Kontaktinfo..

```html
<!DOCTYPE html>
<html lang="de">
<head>
<meta charset="utf-8">
<title>Flyer Freiwillige Feuerwehr</title>
<link href="https://fonts.googleapis.com/css2?family=Oswald:wght@500;600&family=Raleway:wght@300;400;600;700&display=swap" rel="stylesheet">
<style>
  :root{
    --stage:#d2d2d2;
    --olive:#5d7222;
    --blue:#3e69a5;
    --slate:#5a5a5a;
    --mist:#dcdcdc;
    --signal:#9a1b1b;
    --ink:#1d1d1d;
    --paper:#ffffff;
    --photo-night:linear-gradient(135deg,#2b3140,#7a3a30 55%,#c9c6c2);
    --photo-gear:linear-gradient(160deg,#3b3a35,#6d6a4f 50%,#2a2f3d);
    --photo-team:linear-gradient(180deg,#d9c9cf,#c8a9b7 35%,#2b3350 60%,#1f2640);
    --photo-field:linear-gradient(180deg,#7ea6d6,#c9d8e6 50%,#4c6b2c 75%,#6b8a34);
  }
  *{margin:0;padding:0;box-sizing:border-box}
  html,body{width:1200px;height:848px;overflow:hidden;background:var(--stage)}
  body{position:relative;font-family:'Raleway',sans-serif;color:var(--ink)}
  .flyer{position:absolute;top:222px;width:570px;height:403px;overflow:hidden;background:var(--paper);box-shadow:0 6px 14px rgba(0,0,0,.25)}
  .flyer--inside{left:20px}
  .flyer--outside{left:610px}
  .block{position:absolute}
  .photo{position:absolute}
  .headline{font-family:'Oswald',sans-serif;font-weight:600;text-transform:uppercase;letter-spacing:.5px;line-height:1}
  .rule{display:block;width:18px;height:3px;margin:9px 0 12px}
  .rule--white{background:var(--paper)}
  .rule--dark{background:var(--ink)}

  /* inside */
  .panel-intro{left:0;top:0;width:190px;height:403px;background:var(--olive);color:var(--paper)}
  .intro-photo{left:6px;top:6px;width:144px;height:144px;border-radius:50%;background:var(--photo-gear)}
  .intro-vertical{position:absolute;left:22px;bottom:20px;transform-origin:left bottom;transform:rotate(-90deg) translateY(100%);font-size:19px;white-space:nowrap;color:var(--paper)}
  .intro-copy{position:absolute;left:64px;top:168px;width:118px;font-size:10.5px;line-height:1.45}
  .intro-copy .rule{margin:0 0 8px;width:16px}
  .panel-team{left:190px;top:0;width:190px;height:403px;background:var(--mist)}
  .team-content{position:absolute;left:22px;top:40px;width:140px}
  .team-content .headline{font-size:22px}
  .team-lead{font-size:10px;line-height:1.45}
  .team-lead strong{font-weight:700;letter-spacing:.3px}
  .truck-photo{left:190px;top:0;width:200px;height:403px;background:var(--photo-night);clip-path:polygon(0 255px,100% 165px,100% 100%,0 100%)}
  .panel-join{left:380px;top:0;width:190px;height:403px;background:var(--blue);color:var(--paper)}
  .drill-photo{left:380px;top:0;width:190px;height:190px;background:var(--photo-gear);clip-path:polygon(0 0,100% 0,100% 162px,0 176px)}
  .join-content{position:absolute;left:16px;top:184px;width:160px}
  .join-content .headline{font-size:22px}
  .join-copy{font-size:10px;line-height:1.6;letter-spacing:.2px}
  .join-copy strong{font-weight:700;letter-spacing:0}

  /* outside */
  .rescue-photo{left:0;top:0;width:190px;height:260px;background:var(--photo-night)}
  .panel-benefits{left:0;top:0;width:190px;height:403px;background:var(--slate);color:var(--paper);clip-path:polygon(0 225px,100% 165px,100% 100%,0 100%)}
  .benefits-content{position:absolute;left:14px;top:240px;width:140px}
  .benefits-content .headline{font-size:22px}
  .benefits-copy{font-size:10.5px;line-height:1.45}
  .panel-cta{left:180px;top:0;width:200px;height:403px;background:var(--blue);color:var(--paper)}
  .cta-content{position:absolute;left:22px;top:22px;width:160px}
  .cta-content .headline{font-size:22px;text-transform:none}
  .cta-label{font-size:6.5px;font-weight:700;margin-bottom:2px}
  .cta-text{font-size:6.5px;line-height:1.45;margin-bottom:14px}
  .contact-list{list-style:none;margin-top:4px}
  .contact-list li{display:flex;align-items:center;gap:10px;font-size:7px;margin-bottom:5px}
  .contact-list svg{width:10px;height:10px;flex:none}
  .contact-street{font-family:'Oswald',sans-serif;font-weight:500}
  .contact-mail{font-family:'Oswald',sans-serif;font-weight:500;font-size:8px;margin:10px 0 0 30px}
  .field-photo{left:168px;top:240px;width:162px;height:162px;border-radius:50%;background:var(--photo-field)}
  .panel-cover{left:380px;top:0;width:190px;height:403px;background:var(--paper);text-align:center}
  .cover-title{margin-top:18px;font-size:25px;letter-spacing:0;white-space:nowrap;color:var(--olive)}
  .cover-sub{margin-top:6px;font-family:'Oswald',sans-serif;font-weight:500;font-size:12px;white-space:nowrap;color:var(--signal)}
  .cover-photo{left:4px;top:78px;width:182px;height:200px;background:var(--photo-team)}
  .cover-question{position:absolute;left:20px;top:296px;width:150px;font-weight:300;font-size:17px;line-height:1.2;color:var(--ink)}
</style>
</head>
<body>

<section class="flyer flyer--inside" aria-label="Flyer Innenseite">
  <div class="block panel-intro">
    <div class="photo intro-photo" role="img" aria-label="Foto: Feuerwehrmann mit Helm bei technischer Rettung im Fahrzeug"></div>
    <h2 class="headline intro-vertical">Engagiere dich - im Team</h2>
    <div class="intro-copy">
      <span class="rule rule--white"></span>
      <p>Der Flyer muss ansprechend, modern und dynamisch sein, um Jugendliche zu motivieren. Junge Menschen interessieren sich oft für Abenteuer, Teamarbeit und den Beitrag zur Gemeinschaft.</p>
    </div>
  </div>

  <div class="block panel-team">
    <div class="team-content">
      <h2 class="headline">Teamarbeit</h2>
      <span class="rule rule--dark"></span>
      <p class="team-lead"><strong>KAMERADSCHAFT -</strong><br>und eine gute berufliche oder ehrenamtliche Entwicklung betonen.</p>
    </div>
  </div>
  <div class="photo truck-photo" role="img" aria-label="Foto: Löschfahrzeug bei Nacht mit Einsatzkraft im Schneefall"></div>

  <div class="block panel-join">
    <div class="join-content">
      <h2 class="headline">Feuerwehr</h2>
      <span class="rule rule--white"></span>
      <p class="join-copy">WERDE TEIL UNSERES TEAMS UND ERLEBE SPANNENDE ABENTEUER! <strong>– Visuelle Gestaltung: Bilder von jungen Feuerwehrmitgliedern in Aktion (z.B. Übungseinsätze, Abenteuer, Teamwork). Teamgeist!'</strong></p>
    </div>
  </div>
  <div class="photo drill-photo" role="img" aria-label="Foto: Atemschutztrupp bei einer Übung im Gebäude"></div>
</section>

<section class="flyer flyer--outside" aria-label="Flyer Außenseite">
  <div class="photo rescue-photo" role="img" aria-label="Foto: Einsatzkräfte bei einer Fahrzeugrettung"></div>
  <div class="block panel-benefits">
    <div class="benefits-content">
      <h2 class="headline">Teamarbeit</h2>
      <span class="rule rule--white"></span>
      <p class="benefits-copy">Benefits: Überzeuge mit Aspekten wie Weiterbildungsmöglichkeiten, Teamarbeit, Verantwortung und gesellschaftlicher Beitrag.</p>
    </div>
  </div>

  <div class="block panel-cta">
    <div class="cta-content">
      <h2 class="headline">Call to Action</h2>
      <span class="rule rule--white"></span>
      <p class="cta-label">Call to Action (CTA):</p>
      <p class="cta-text">Komm zu uns! Wir suchen dich – Melde dich noch heute an!'</p>
      <p class="cta-label">Anmeldung</p>
      <p class="cta-text">Donnerstag 10.00 - 18.00 Uhr<br>Freitag 10.00 - 18.00 Uhr</p>
      <ul class="contact-list">
        <li>
          <svg viewBox="0 0 10 10" fill="none" stroke="#fff" stroke-width=".8"><path d="M5 9.3C3 6.8 2 5.2 2 3.8a3 3 0 0 1 6 0c0 1.4-1 3-3 5.5z"/><circle cx="5" cy="3.8" r="1"/></svg>
          <span class="contact-street">Lindenstraße 14</span>
        </li>
        <li>
          <svg viewBox="0 0 10 10" fill="none" stroke="#fff" stroke-width=".8"><rect x="1" y="2.5" width="8" height="5.5"/><path d="M1 2.5l4 3.2 4-3.2"/></svg>
          <span>27412 Lindenau</span>
        </li>
        <li>
          <svg viewBox="0 0 10 10" fill="none" stroke="#fff" stroke-width=".8"><path d="M2.2 1.2l1.6 1.6-.9 1.3a6 6 0 0 0 3 3l1.3-.9 1.6 1.6-1 1A7 7 0 0 1 1.2 2.2z"/></svg>
          <span>04721 | 765432</span>
        </li>
      </ul>
      <p class="contact-mail">kontakt@wehr-lindenau.de</p>
    </div>
  </div>
  <div class="photo field-photo" role="img" aria-label="Foto: Jugendfeuerwehr beim Löschangriff auf einer Wiese"></div>

  <div class="block panel-cover">
    <h1 class="headline cover-title">Engagiere dich</h1>
    <p class="cover-sub">Deine Feuerwehr braucht dich!</p>
    <div class="photo cover-photo" role="img" aria-label="Foto: vier junge Feuerwehrmitglieder legen die Hände zusammen vor blühendem Baum"></div>
    <p class="cover-question">Möchtest du nur zusehen oder live dabei sein?</p>
  </div>
</section>

</body>
</html>
```